Luxury artist needs high end & clean shopify website for selling prints

PLEASE REVIEW IN DETAIL DESIGN BRIEF IN UPLOADS
A luxury artist is in need of a high-end, clean, and aesthetically pleasing Shopify website to showcase and sell their unique prints. This website must reflect the upscale nature of the artist's work, with a focus on a polished, minimalist design that allows the art to take center stage.
The website should feature a user-friendly interface and seamless navigation to ensure a superior shopping experience for visitors. It should also include a secure and hassle-free checkout process, along with options for various payment methods.
In addition, the website should have features such as zoom-in capabilities to allow potential buyers to view the intricate details of each print, a section for customer reviews, and an about page detailing the artist's journey and inspiration.
Ultimately, this website will be more than just a sales platform; it will be an online gallery that represents the artist's brand, entices art enthusiasts, and facilitates the easy purchase of high-quality prints.
High end luxury art buyer

```html
<!DOCTYPE html>
<html lang="en">
<head>
<meta charset="utf-8">
<title>Parietal — Fine Art Prints</title>
<link rel="stylesheet" href="https://fonts.googleapis.com/css2?family=Playfair+Display:wght@400;600;700&family=Poppins:wght@300;400;500&display=swap">
<style>
:root{
  --ink:#111111;
  --night:#1a1c1f;
  --green:#1f3a2b;
  --taupe:#9b8c80;
  --mist:#efefef;
  --line:#cfcfcf;
  --white:#ffffff;
  --muted:#5a5a5a;
}
*{box-sizing:border-box;margin:0;padding:0}
html,body{width:1200px;height:5196px;overflow:hidden}
body{position:relative;background:var(--white);color:var(--ink);font-family:"Poppins",sans-serif}
.section{position:absolute;left:0;width:1200px}
.abs{position:absolute}
.heading{font-family:"Playfair Display",serif;font-weight:700;font-size:38px;letter-spacing:1px;text-transform:uppercase;white-space:nowrap}
.heading-rule{position:absolute;height:3px;width:80px;background:var(--ink)}
.btn{position:absolute;display:flex;align-items:center;justify-content:center;gap:14px;background:var(--green);color:var(--white);border-radius:30px;font-family:"Playfair Display",serif;font-size:19px;white-space:nowrap}
.ph{position:absolute}

/* header */
.site-header{top:0;height:72px;background:var(--white);z-index:3}
.brand-tab{position:absolute;left:0;top:0;width:360px;height:130px;background:var(--white);border-bottom-right-radius:60px;z-index:4;display:flex;align-items:center;justify-content:center;gap:12px}
.brand-dot{width:14px;height:14px;border-radius:50%;background:var(--ink)}
.brand-name{font-family:"Playfair Display",serif;font-weight:600;font-size:40px;color:var(--ink)}
.main-nav{position:absolute;left:405px;top:22px;display:flex;gap:38px;font-family:"Playfair Display",serif;font-size:16px;font-weight:600;white-space:nowrap}

/* hero */
.hero{top:0;height:630px;background:linear-gradient(120deg,#2b2e33 0%,#1c1f24 45%,#0b0c0e 100%)}
.hero-welcome{left:100px;top:236px;font-family:"Playfair Display",serif;font-size:46px;color:var(--white)}
.hero-title{left:100px;top:292px;font-family:"Playfair Display",serif;font-weight:600;font-size:72px;letter-spacing:2px;color:var(--white)}
.hero-tag{left:100px;top:392px;font-family:"Playfair Display",serif;font-size:19px;color:var(--white)}
.hero-art-frame{left:790px;top:80px;width:320px;height:500px;background:var(--white);transform:rotate(-3deg);padding:16px}

/* about */
.about{top:700px;height:720px}
.about-photo-frame{left:128px;top:110px;width:440px;height:570px;border:3px solid var(--white);z-index:2}
.about-body{left:600px;top:200px;width:540px;font-size:16px;line-height:1.6;color:var(--muted)}
.about-body p{margin-bottom:20px}

/* products */
.products{top:1460px;height:600px;background:var(--taupe)}
.product-card{position:absolute;top:180px;height:340px;background:var(--ink);border-radius:8px;overflow:hidden}
.product-info{position:absolute;left:0;bottom:0;width:100%;height:82px;padding:14px 16px;color:var(--white)}
.product-row{display:flex;justify-content:space-between;font-family:"Playfair Display",serif;font-size:16px;font-weight:700;white-space:nowrap}
.product-buy{display:flex;justify-content:space-between;margin-top:14px;font-size:13px}
.arrow-round{position:absolute;width:62px;height:62px;border-radius:50%;background:var(--ink);display:flex;align-items:center;justify-content:center}

/* gallery */
.gallery{top:2080px;height:640px}
.gallery-item{position:absolute;border-radius:12px;overflow:hidden}

/* blog */
.blog{top:2760px;height:580px;background:var(--mist)}
.blog-card{position:absolute;top:148px;width:520px;height:422px;background:var(--ink);border-radius:12px;overflow:hidden;color:var(--white)}
.blog-text{position:absolute;left:20px;top:250px;width:480px}
.blog-title{font-family:"Playfair Display",serif;font-weight:700;font-size:17px;text-transform:uppercase}
.blog-meta{margin-top:14px;font-size:12px;line-height:1.6;color:#cfcfcf}
.blog-link{margin-top:18px;font-size:15px;display:flex;align-items:center;gap:10px}

/* contact */
.contact{top:3340px;height:680px}
.field{position:absolute;height:44px;border:1px solid var(--line);border-radius:10px;background:var(--white);font-size:14px;padding:12px 14px;color:#333}

/* newsletter */
.newsletter{top:4032px;height:300px;background:linear-gradient(180deg,#26282c,#121316)}
.news-input{left:260px;top:178px;width:470px;height:46px;border-radius:24px;background:var(--white);font-size:15px;padding:13px 22px}

/* testimonials */
.testimonials{top:4400px;height:540px}
.quote{left:600px;top:130px;width:540px;font-size:15px;line-height:1.6;color:var(--muted)}

/* footer */
.site-footer{top:4960px;height:236px;background:var(--ink);color:var(--white)}
.footer-brand{left:100px;top:84px;display:flex;align-items:center;gap:16px}
.footer-brand .brand-dot{background:var(--white);width:18px;height:18px}
.footer-brand .brand-name{color:var(--white);font-size:56px}
</style>
</head>
<body>

<section class="section hero">
  <div class="ph hero-art-frame">
    <div role="img" aria-label="Black and white painting of dancing figures" style="width:100%;height:100%;background:linear-gradient(160deg,#e9e9e9,#8d8d8d 50%,#d8d8d8)"></div>
  </div>
  <div class="abs hero-welcome">Welcome To</div>
  <div class="abs hero-title">PARIETAL</div>
  <div class="abs hero-tag">Turning Body Language Into Tangible Pieces Of Art</div>
  <a class="btn" style="left:100px;top:440px;width:190px;height:52px">Buy Now
    <svg width="26" height="12" viewBox="0 0 26 12"><path d="M0 6h22M17 1l6 5-6 5" stroke="#fff" stroke-width="2" fill="none"/></svg></a>
</section>

<header class="section site-header">
  <nav class="main-nav"><span>Home</span><span>Original Artwork</span><span>Reproductions</span><span>Events Exhibitions</span><span>The Artist Contact</span></nav>
</header>
<div class="brand-tab"><span class="brand-dot"></span><span class="brand-name">Parietal</span></div>

<section class="section about">
  <div class="ph" role="img" aria-label="Black and white portrait of the artist" style="left:100px;top:72px;width:440px;height:580px;background:linear-gradient(180deg,#5a5a5a,#1d1d1d)"></div>
  <div class="abs about-photo-frame"></div>
  <div class="abs heading" style="left:600px;top:90px">About Us</div>
  <div class="heading-rule" style="left:600px;top:148px"></div>
  <div class="abs about-body">
    <p>My work features expressive lines in high contrast to spark the visual processing centre of the brain, the parietal lobe. The name I gave myself, Parietal, is not only connected with my art because of its visual nature, but also because the word itself is strong and accurately represents my personal muse.</p>
    <p>Initially, creating art was an outlet to express emotion. Now, it's become how I find endless ways to share the memories and vibes of one of my favorite human beings with the world. She lived a vibrant life and it's my aim to ensure her presence lives on through a sense as meaningful as art.</p>
  </div>
  <a class="btn" style="left:600px;top:580px;width:190px;height:52px">Read More
    <svg width="26" height="12" viewBox="0 0 26 12"><path d="M0 6h22M17 1l6 5-6 5" stroke="#fff" stroke-width="2" fill="none"/></svg></a>
</section>

<section class="section products">
  <div class="abs heading" style="left:100px;top:52px;color:var(--ink)">Our Products</div>
  <div class="heading-rule" style="left:100px;top:104px"></div>
  <svg class="abs" style="left:980px;top:80px" width="60" height="14" viewBox="0 0 60 14"><path d="M60 7H4M10 1L3 7l7 6" stroke="#d8d0c9" stroke-width="2" fill="none"/></svg>
  <div class="arrow-round" style="left:1040px;top:56px"><svg width="26" height="14" viewBox="0 0 26 14"><path d="M0 7h22M16 1l7 6-7 6" stroke="#fff" stroke-width="2.4" fill="none"/></svg></div>

  <div class="product-card" style="left:100px;width:240px">
    <div role="img" aria-label="Canvas print of a city skyline" style="height:258px;background:linear-gradient(180deg,#d9d4cf,#6f6258 60%,#9a3b2a)"></div>
    <div class="product-info"><div class="product-row"><span>Canvas Prints</span><span>$25.22</span></div><div class="product-buy"><span>Buy Now</span><span>&#9636;</span></div></div>
  </div>
  <div class="product-card" style="left:360px;width:228px">
    <div role="img" aria-label="Metal sculpture print of a horse" style="height:258px;background:linear-gradient(180deg,#c9d8e6,#7a5236 55%,#c7b49a)"></div>
    <div class="product-info"><div class="product-row"><span>Metal Sculptures</span><span>$25.22</span></div><div class="product-buy"><span>Buy Now</span><span>&#9636;</span></div></div>
  </div>
  <div class="product-card" style="left:600px;width:240px">
    <div role="img" aria-label="Colourful abstract gouache painting" style="height:258px;background:linear-gradient(135deg,#e08a2c,#d64a2f 40%,#3f7fb3 75%,#f0e1b6)"></div>
    <div class="product-info"><div class="product-row"><span>Gouache Paintings</span><span>$25.22</span></div><div class="product-buy"><span>Buy Now</span><span>&#9636;</span></div></div>
  </div>
  <div class="product-card" style="left:852px;width:244px">
    <div role="img" aria-label="Large format print on paper in a print shop" style="height:258px;background:linear-gradient(180deg,#2a2f3a,#8a4a5e 50%,#dcd8e2)"></div>
    <div class="product-info"><div class="product-row"><span>Prints On Paper</span><span>$25.22</span></div><div class="product-buy"><span>Buy Now</span><span>&#9636;</span></div></div>
  </div>
  <svg class="abs" style="left:224px;top:542px" width="12" height="12"><circle cx="6" cy="6" r="5" fill="none" stroke="#ffffff" stroke-width="1.5"/></svg>
</section>

<section class="section gallery">
  <div class="abs heading" style="left:0;width:1200px;text-align:center;top:56px">Our Gallery</div>
  <div class="heading-rule" style="left:560px;top:110px"></div>
  <div class="gallery-item" role="img" aria-label="Exhibition wall with framed black and white art" style="left:-20px;top:220px;width:240px;height:300px;background:linear-gradient(180deg,#cfcfcf,#6e6e6e)"></div>
  <div class="gallery-item" role="img" aria-label="Gallery room with framed drawings" style="left:240px;top:200px;width:240px;height:340px;background:linear-gradient(180deg,#e2e2e2,#8c8c8c)"></div>
  <div class="gallery-item" role="img" aria-label="White gallery hall with artworks" style="left:500px;top:170px;width:240px;height:300px;background:linear-gradient(180deg,#f0f0f0,#a0a0a0)"></div>
  <div class="gallery-item" role="img" aria-label="Visitors viewing framed artwork" style="left:768px;top:200px;width:240px;height:340px;background:linear-gradient(180deg,#d8d2cc,#4a4846)"></div>
  <div class="gallery-item" role="img" aria-label="Dark room with illuminated figure artwork" style="left:1032px;top:230px;width:200px;height:260px;background:linear-gradient(180deg,#1b1b1b,#6a6a6a)"></div>
</section>

<section class="section blog">
  <div class="abs heading" style="left:100px;top:50px">Our Blog</div>
  <div class="heading-rule" style="left:100px;top:102px"></div>
  <svg class="abs" style="left:980px;top:74px" width="60" height="14" viewBox="0 0 60 14"><path d="M60 7H4M10 1L3 7l7 6" stroke="#999" stroke-width="2" fill="none"/></svg>
  <div class="arrow-round" style="left:1040px;top:50px"><svg width="26" height="14" viewBox="0 0 26 14"><path d="M0 7h22M16 1l7 6-7 6" stroke="#fff" stroke-width="2.4" fill="none"/></svg></div>

  <article class="blog-card" style="left:100px">
    <div role="img" aria-label="Outdoor festival tent displaying framed art" style="height:232px;background:linear-gradient(180deg,#a9c6e2,#e9ecef 45%,#6f8a5a)"></div>
    <div class="blog-text">
      <div class="blog-title">Harbor Museum Outdoor Arts Festival</div>
      <div class="blog-meta">Sat, Oct 5, 2024 10:00 AM – Sun, Oct 6, 2024 5:00 PM | Harbor Museum Lawn, 12 Pier Road, Marlow Bay, CT</div>
      <div class="blog-link">View Event <svg width="22" height="10" viewBox="0 0 22 10"><path d="M0 5h19M14 1l5 4-5 4" stroke="#fff" stroke-width="1.6" fill="none"/></svg></div>
    </div>
  </article>
  <article class="blog-card" style="left:660px">
    <div role="img" aria-label="Festival booth showing framed figure drawings" style="height:232px;background:linear-gradient(180deg,#c8c8c8,#5c5c5c)"></div>
    <div class="blog-text">
      <div class="blog-title">Seabrook Beach Festival of the Arts</div>
      <div class="blog-meta">Sat, Aug 3, 2024 10:00 AM – Sun, Aug 4, 2024 5:00 PM | Main Street Green, Seabrook, NY</div>
      <div class="blog-link">View Event <svg width="22" height="10" viewBox="0 0 22 10"><path d="M0 5h19M14 1l5 4-5 4" stroke="#fff" stroke-width="1.6" fill="none"/></svg></div>
    </div>
  </article>
</section>

<section class="section contact">
  <div role="img" aria-label="Faint dotted world map" style="position:absolute;left:100px;top:60px;width:1000px;height:520px;background:radial-gradient(ellipse at center,#e4e4e4 0%,#f6f6f6 55%,#ffffff 75%)"></div>
  <div class="abs heading" style="left:0;width:1200px;text-align:center;top:136px">Contact Us</div>
  <div class="heading-rule" style="left:560px;top:190px"></div>
  <div class="field" style="left:200px;top:240px;width:392px">First Name</div>
  <div class="field" style="left:612px;top:240px;width:392px">Last Name</div>
  <div class="field" style="left:200px;top:300px;width:392px">Phone number</div>
  <div class="field" style="left:612px;top:300px;width:392px">Email Address</div>
  <div class="field" style="left:200px;top:372px;width:804px;height:120px">Message</div>
  <a class="btn" style="left:500px;top:530px;width:200px;height:52px">Send Now</a>
</section>

<section class="section newsletter">
  <div class="abs heading" style="left:0;width:1200px;text-align:center;top:56px;color:var(--white);font-weight:600">Sign Up For The Newsletter</div>
  <div class="heading-rule" style="left:560px;top:112px;background:var(--white)"></div>
  <div class="abs news-input">Enter Email</div>
  <a class="btn" style="left:740px;top:178px;width:200px;height:46px;font-size:16px;border-radius:24px">SIGN UP</a>
</section>

<section class="section testimonials">
  <div style="position:absolute;left:128px;top:70px;width:440px;height:420px;background:var(--ink)"></div>
  <div class="ph" role="img" aria-label="Blank canvases leaning in a bright studio" style="left:100px;top:40px;width:440px;height:420px;background:linear-gradient(180deg,#efefef,#b9b5b1)"></div>
  <div class="abs heading" style="left:600px;top:42px">Testimonials</div>
  <div class="heading-rule" style="left:600px;top:96px"></div>
  <div class="abs quote">Each print arrived beautifully packed and the detail is even richer in person. The line work feels alive on my wall, and the whole ordering process was calm, personal and effortless. Guests ask about it every time they visit my home, and I already plan to order more.</div>
  <div role="img" aria-label="Client portrait" style="position:absolute;left:604px;top:300px;width:58px;height:58px;border-radius:50%;background:linear-gradient(180deg,#9a9a9a,#4a4a4a)"></div>
  <div class="abs" style="left:678px;top:302px;font-family:'Playfair Display',serif;font-weight:700;font-size:18px">Mara Lind</div>
  <div class="abs" style="left:678px;top:332px;font-size:14px;color:var(--muted)">Client</div>
  <svg class="abs" style="left:820px;top:322px" width="40" height="12" viewBox="0 0 40 12"><path d="M40 6H4M9 1L3 6l6 5" stroke="#999" stroke-width="1.6" fill="none"/></svg>
  <div class="arrow-round" style="left:870px;top:310px;width:36px;height:36px"><svg width="16" height="10" viewBox="0 0 16 10"><path d="M0 5h13M9 1l4 4-4 4" stroke="#fff" stroke-width="1.6" fill="none"/></svg></div>
</section>

<footer class="section site-footer">
  <div class="abs footer-brand"><span class="brand-dot"></span><span class="brand-name">Parietal</span></div>
  <div class="abs" style="left:720px;top:150px;font-size:15px;white-space:nowrap">© copyrights 2023 Parietal | All Rights Reserved</div>
  <svg class="abs" style="left:960px;top:78px" width="100" height="46" viewBox="0 0 100 46">
    <circle cx="22" cy="23" r="20" fill="none" stroke="#c9416e" stroke-width="2"/>
    <circle cx="74" cy="23" r="20" fill="none" stroke="#4a6fd1" stroke-width="2"/>
  </svg>
</footer>

</body>
</html>
```